Zephyr Quill - Dog Supplement Brand

Here a link to a word doc with all of my info.
Please read it carefully.
https://files.brindlemoor.net/page/d/7tRkWpLzQ2mNvA84xHcYbEuJ0sFdKo93Tg5LhPq-2/view?ref=open
Its 2 pages. Home Page and Product Page.
Oh and btw: the poses I attached dont have a shadow, so it would be good if you added a shadow to the poses .
If you have any questions please let me know.
Target Market(s)
Dog Owners In UK
Industry/Entity Type
Dog supplements
Number of Pages Required
2 page
Requirements
Must have
- Home page and product page files. Super Hero Theme.

```html
<!DOCTYPE html>
<html lang="en">
<head>
<meta charset="utf-8">
<title>Zephyr Quill – Home</title>
<link href="https://fonts.googleapis.com/css2?family=Poppins:wght@400;500;600;700;800;900&display=swap" rel="stylesheet">
<style>
:root{
  --coral:#ea5a4f;
  --blue:#1e3eb0;
  --blue-deep:#182f92;
  --yellow:#f6c52a;
  --orange:#f39420;
  --red:#e9574b;
  --sky:#2db9f0;
  --green:#6cc25a;
  --green-dark:#57ad46;
  --ink:#141414;
  --text:#4a4a4a;
  --white:#ffffff;
  --muted:#f3f3f3;
  --fig:#e9e9ee;
}
*{margin:0;padding:0;box-sizing:border-box}
html,body{width:1200px;height:5128px;overflow:hidden}
body{font-family:"Poppins",sans-serif;color:var(--ink);background:var(--white);position:relative}
.abs{position:absolute}
.btn{position:absolute;display:flex;align-items:center;justify-content:center;gap:8px;background:var(--green);color:#fff;font-weight:700;font-size:13px;text-transform:uppercase;border-radius:30px;box-shadow:0 4px 0 var(--green-dark),0 8px 16px rgba(0,0,0,.15);letter-spacing:.3px}
.paw{width:16px;height:16px}
.figure{position:absolute;border-radius:28px}

.promo{top:0;left:0;width:1200px;height:28px;background:var(--coral);color:#fff;font-size:10px;font-weight:600;display:flex;align-items:center;justify-content:center;letter-spacing:.2px}
.header{top:28px;left:0;width:1200px;height:96px;background:#fff}
.menu-btn{left:88px;top:26px;display:flex;align-items:center;gap:12px;font-size:11px;font-weight:700}
.menu-btn .ic{width:44px;height:44px;border-radius:50%;background:var(--muted);display:flex;align-items:center;justify-content:center}
.logo{left:0;width:1200px;top:30px;text-align:center;font-weight:900;font-size:30px;letter-spacing:-.5px}
.header-icons{right:90px;top:34px;display:flex;gap:26px;align-items:center}

.hero{top:124px;left:0;width:1200px;height:680px;background:radial-gradient(circle at 70% 40%,#2b52d0 0%,var(--blue) 45%,var(--blue-deep) 100%);overflow:hidden}
.hero-scallop{left:0;top:730px;width:1200px;height:80px;background:radial-gradient(circle at 50% 100%,#fff 58px,transparent 59px) repeat-x;background-size:110px 80px}
.hero-title{left:734px;top:252px;color:#fff;font-weight:900;font-size:92px;line-height:.9;letter-spacing:-3px}
.hero-tag{left:732px;top:474px;color:#fff;font-size:22px;line-height:1.4;width:400px}

.h-big{font-weight:900;text-transform:uppercase;line-height:1.02;letter-spacing:-.5px}
.body-copy{font-size:15px;line-height:1.8;color:var(--text)}

.offer{top:1520px;left:0;width:1200px;height:490px;background:linear-gradient(180deg,var(--orange) 0%,#f7b224 70%,var(--yellow) 100%)}
.offer-scallop{top:1510px;left:0;width:1200px;height:60px;background:radial-gradient(circle at 50% 0%,#fff 36px,transparent 37px) repeat-x;background-size:72px 60px}
.section-title{left:0;width:1200px;text-align:center;font-weight:900;font-size:46px;text-transform:uppercase;letter-spacing:-.5px}
.rule{width:44px;height:3px;left:578px}
.card{position:absolute;top:1820px;width:246px;height:290px;background:#fff;border-radius:22px;box-shadow:0 12px 30px rgba(0,0,0,.10);text-align:center;padding-top:86px}
.card h3{font-size:18px;font-weight:700;line-height:1.45}
.card p{font-size:12.5px;color:var(--text);line-height:1.6;margin:14px 30px 0}
.card .arrow{width:34px;height:34px;border-radius:50%;background:var(--muted);margin:22px auto 0;display:flex;align-items:center;justify-content:center}
.card-photo{position:absolute;top:1740px;width:140px;height:140px;border-radius:50%;border:6px solid #fff;box-shadow:0 6px 16px rgba(0,0,0,.15)}

.review{position:absolute;top:2476px;width:330px;height:206px;background:#fff;border-radius:10px;box-shadow:0 10px 30px rgba(0,0,0,.09);padding:72px 26px 0}
.review p{font-size:13px;line-height:1.7;color:var(--text)}
.review .who{display:flex;justify-content:space-between;align-items:center;margin-top:22px;font-size:13px;font-weight:700}
.stars{color:#f6b817;font-size:17px;letter-spacing:1px}
.avatar{position:absolute;top:-34px;left:34px;width:72px;height:72px;border-radius:50%;border:5px solid #fff;background:#b08a74}
.quote{position:absolute;top:16px;left:150px;font-size:90px;font-weight:900;color:#ececec;line-height:1}

.vets{top:2850px;left:0;width:1200px;height:470px;background:var(--red);overflow:hidden}
.vets-scallop{top:2800px;left:0;width:1200px;height:80px;background:radial-gradient(circle at 50% 100%,var(--red) 48px,transparent 49px) repeat-x;background-size:96px 80px}
.ghost{left:-20px;top:3040px;font-weight:900;font-size:230px;color:rgba(255,255,255,.14);letter-spacing:6px;white-space:nowrap;line-height:1}

.why{top:4180px;left:0;width:1200px;height:470px;background:linear-gradient(180deg,#2ab4ee,var(--sky))}
.why-scallop{top:4140px;left:0;width:1200px;height:80px;background:radial-gradient(circle at 50% 100%,#2ab4ee 46px,transparent 47px) repeat-x;background-size:84px 80px}
.feature{position:absolute;top:4406px;width:160px;text-align:center;color:#fff;font-weight:700;font-size:15px;line-height:1.35}
.feature .icon{width:96px;height:96px;margin:0 auto 14px;border-radius:50%;background:rgba(255,255,255,.95);display:flex;align-items:center;justify-content:center}

.flabel{font-size:10px;font-weight:700;text-transform:uppercase}
.select{left:160px;top:5010px;width:236px;height:44px;border:1px solid #d6d6d6;border-radius:22px;font-size:12px;display:flex;align-items:center;justify-content:space-between;padding:0 18px}
.pay{display:flex;gap:9px;left:616px;top:5018px}
.pay i{display:block;width:34px;height:22px;border-radius:4px;background:#e4e4e4;border:1px solid #cfcfcf}
</style>
</head>
<body>

<div class="abs promo">FREE SHIPPING ON ALL ORDERS OVER £20 +++ GET YOUR FIRST BOTTLE FOR JUST £10 WHEN YOU JOIN FORCES!</div>

<header class="abs header">
  <div class="abs menu-btn"><span class="ic"><svg width="18" height="14" viewBox="0 0 18 14"><path d="M1 1h16M1 7h16M1 13h16" stroke="#141414" stroke-width="2" stroke-linecap="round"/></svg></span>MENU</div>
  <div class="abs logo">ZEPHYR QUILL</div>
  <div class="abs header-icons">
    <svg width="20" height="20" viewBox="0 0 20 20"><circle cx="8" cy="8" r="6" stroke="#141414" stroke-width="2.4" fill="none"/><path d="M13 13l5 5" stroke="#141414" stroke-width="2.6" stroke-linecap="round"/></svg>
    <svg width="20" height="20" viewBox="0 0 20 20"><circle cx="10" cy="6" r="4.5" fill="#141414"/><path d="M2 19c0-5 4-7 8-7s8 2 8 7z" fill="#141414"/></svg>
    <svg width="26" height="24" viewBox="0 0 26 24"><path d="M1 2h4l3 13h12l3-9H7" stroke="#141414" stroke-width="2.2" fill="none" stroke-linejoin="round"/><circle cx="10" cy="20" r="2" fill="#141414"/><circle cx="18" cy="20" r="2" fill="#141414"/><circle cx="22" cy="3" r="6" fill="var(--green)"/><text x="22" y="6" font-size="8" fill="#fff" text-anchor="middle" font-family="Poppins,sans-serif">0</text></svg>
  </div>
</header>

<section class="abs hero"></section>
<div class="abs hero-scallop"></div>
<div class="figure" role="img" aria-label="Hero illustration: superhero husky mascot in red cape flying in front of a yellow comic cloud, with a soft shadow" style="left:44px;top:170px;width:620px;height:800px;background:linear-gradient(180deg,#f6c52a 0%,#f3d56a 35%,#e9e9ee 60%,#f2f2f5 100%);box-shadow:0 26px 36px rgba(0,0,0,.14)"></div>
<div class="abs hero-title">ZEPHYR<br>QUILL</div>
<div class="abs hero-tag">Join forces with zephyr quill &amp; let him be your beloved dog's hero!</div>
<div class="btn" style="left:736px;top:560px;width:180px;height:48px"><svg class="paw" viewBox="0 0 16 16"><ellipse cx="8" cy="11" rx="4" ry="3.4" fill="#fff"/><circle cx="3" cy="6.5" r="1.7" fill="#fff"/><circle cx="6" cy="3.5" r="1.7" fill="#fff"/><circle cx="10" cy="3.5" r="1.7" fill="#fff"/><circle cx="13" cy="6.5" r="1.7" fill="#fff"/></svg>Join forces!</div>

<div class="abs h-big" style="left:126px;top:1040px;font-size:48px">HI! I'M ZEPHYR<br>QUILL!</div>
<p class="abs body-copy" style="left:126px;top:1168px;width:430px">Lorem ipsum dolor sit amet, consectetur adipisicing elit, sed do eiusmod tempor incididunt ut labore et dolore magna aliqua. Ut enim ad minim veniam, quis nostrud exercitation ullamco laboris nisi ut aliquip ex ea commodo consequat...</p>
<div class="btn" style="left:124px;top:1334px;width:200px;height:44px;font-size:12px">Read more about me</div>
<div class="figure" role="img" aria-label="Husky mascot waving, wearing red cape and gold emblem, with soft shadow" style="left:600px;top:910px;width:400px;height:550px;background:linear-gradient(180deg,#ececf0 0%,#f1f1f4 100%);box-shadow:0 20px 30px rgba(0,0,0,.12)"></div>

<section class="abs offer"></section>
<div class="abs offer-scallop"></div>
<div class="abs" style="top:2010px;left:0;width:1200px;height:20px;background:#fff"></div>
<h2 class="abs section-title" style="top:1640px;color:#fff">HERE'S WHAT I OFFER</h2>
<div class="abs rule" style="top:1712px;background:#fff"></div>

<div class="card" style="left:90px"><h3>Zephyr Quill<br>Joint Support</h3><p>Our Zephyr Quill – Calm keeps your dog's nerves in check, helping them.</p><div class="arrow"><svg width="12" height="10" viewBox="0 0 12 10"><path d="M1 5h10M7 1l4 4-4 4" stroke="#141414" stroke-width="1.6" fill="none"/></svg></div></div>
<div class="card" style="left:348px"><h3>Zephyr Quill<br>MultiVits</h3><p>Our Zephyr Quill – Calm keeps your dog's nerves in check, helping them.</p><div class="arrow"><svg width="12" height="10" viewBox="0 0 12 10"><path d="M1 5h10M7 1l4 4-4 4" stroke="#141414" stroke-width="1.6" fill="none"/></svg></div></div>
<div class="card" style="left:606px"><h3>Zephyr Quill<br>Probiotics</h3><p>Our Zephyr Quill – Calm keeps your dog's nerves in check, helping them.</p><div class="arrow"><svg width="12" height="10" viewBox="0 0 12 10"><path d="M1 5h10M7 1l4 4-4 4" stroke="#141414" stroke-width="1.6" fill="none"/></svg></div></div>
<div class="card" style="left:864px"><h3>Zephyr Quill<br>Calm</h3><p>Our Zephyr Quill – Calm keeps your dog's nerves in check, helping them.</p><div class="arrow"><svg width="12" height="10" viewBox="0 0 12 10"><path d="M1 5h10M7 1l4 4-4 4" stroke="#141414" stroke-width="1.6" fill="none"/></svg></div></div>
<div class="card-photo" role="img" aria-label="Terrier dog photo on orange" style="left:143px;background:#ef8a4c"></div>
<div class="card-photo" role="img" aria-label="Vizsla dog photo on teal" style="left:401px;background:#27b6ae"></div>
<div class="card-photo" role="img" aria-label="Chihuahua dog photo on purple" style="left:659px;background:#9b38d4"></div>
<div class="card-photo" role="img" aria-label="Golden retriever photo on pink" style="left:917px;background:#ee6ea8"></div>

<div class="btn" style="left:487px;top:2158px;width:226px;height:44px;font-size:12px">View all product labels</div>

<h2 class="abs h-big" style="left:0;width:1200px;text-align:center;top:2290px;font-size:44px">PEOPLE LOVE ME</h2>
<div class="abs rule" style="top:2354px;background:#ddd"></div>
<div class="abs" style="left:1068px;top:2310px;display:flex;gap:6px;align-items:center">
  <span style="width:10px;height:10px;border-radius:50%;border:1.5px solid #bbb"></span>
  <span style="width:12px;height:12px;border-radius:50%;border:3px solid #141414"></span>
  <span style="width:10px;height:10px;border-radius:50%;border:1.5px solid #bbb"></span>
</div>
<div class="figure" role="img" aria-label="Husky mascot giving a thumbs up in front of a purple comic burst, with soft shadow" style="left:40px;top:2310px;width:300px;height:450px;background:linear-gradient(180deg,#5a40cc 0%,#8f84dc 40%,#ececf0 70%,#f1f1f4 100%);box-shadow:0 20px 28px rgba(0,0,0,.12)"></div>

<div class="review" style="left:404px"><div class="avatar"></div><div class="quote">“</div><p>Africa needs more of such projects in order to tackle the massive malnutrition problems of its populations...</p><div class="who"><span>Marta Okonde</span><span class="stars">★★★★★</span></div></div>
<div class="review" style="left:750px"><div class="avatar" style="background:#4e6782"></div><div class="quote">“</div><p>Africa needs more of such projects in order to tackle the massive malnutrition problems of its populations...</p><div class="who"><span>Owen Harlow</span><span class="stars">★★★★★</span></div></div>
<div class="review" style="left:1096px"><div class="avatar" style="background:#8d7262"></div><div class="quote">“</div><p>Africa needs more of such projects in order to tackle the massive malnutrition problems of its populations...</p><div class="who"><span>Priya Venn</span><span class="stars">★★★★★</span></div></div>

<div class="abs vets-scallop"></div>
<section class="abs vets"></section>
<div class="abs ghost">VIDEO PLAY</div>
<h2 class="abs section-title" style="top:2944px;color:#fff">APPROVED BY EXPERT VETS</h2>
<div class="abs rule" style="top:3012px;background:#fff"></div>
<div class="figure" role="img" aria-label="Video thumbnail: chihuahua close-up inside a blue thought cloud" style="left:270px;top:3040px;width:660px;height:520px;background:linear-gradient(180deg,#8cc9ea 0%,#6fb8e1 100%);box-shadow:0 10px 30px rgba(0,0,0,.15)"></div>
<div class="abs" style="left:764px;top:3318px;width:68px;height:68px;border-radius:50%;background:rgba(90,120,140,.6);display:flex;align-items:center;justify-content:center"><svg width="20" height="22" viewBox="0 0 20 22"><path d="M3 2l15 9-15 9z" fill="#fff"/></svg></div>

<div class="abs h-big" style="left:126px;top:3650px;font-size:48px">REGULATED &amp;<br>CERTIFIED</div>
<p class="abs body-copy" style="left:126px;top:3782px;width:430px">Lorem ipsum dolor sit amet, consectetur adipisicing elit, sed do eiusmod tempor incididunt ut labore et dolore magna aliqua. Ut enim ad minim veniam, quis nostrud exercitation ullamco laboris nisi ut aliquip ex ea commodo consequat...</p>
<div class="abs" style="left:126px;top:3930px;display:flex;gap:22px">
  <span style="width:64px;height:64px;border-radius:50%;border:3px solid #333;background:#fafafa"></span>
  <span style="width:64px;height:64px;border-radius:50%;border:3px solid #333;background:var(--green)"></span>
  <span style="width:64px;height:64px;border-radius:50%;border:3px solid #333;background:#fafafa"></span>
</div>
<div class="figure" role="img" aria-label="Husky mascot in lab coat and goggles holding a test tube, with soft shadow" style="left:620px;top:3540px;width:400px;height:520px;background:linear-gradient(180deg,#ececf0 0%,#f1f1f4 100%);box-shadow:0 20px 30px rgba(0,0,0,.12)"></div>

<div class="abs why-scallop"></div>
<section class="abs why"></section>
<h2 class="abs section-title" style="top:4300px;color:#fff">WHY CHOOSE ME?</h2>
<div class="abs rule" style="top:4366px;background:#fff"></div>
<div class="feature" style="left:80px"><div class="icon"><svg width="56" height="40" viewBox="0 0 56 40"><rect x="2" y="6" width="32" height="22" rx="2" fill="var(--green)"/><path d="M34 12h12l8 8v8H34z" fill="var(--green)"/><circle cx="12" cy="32" r="5" fill="var(--green)"/><circle cx="44" cy="32" r="5" fill="var(--green)"/></svg></div>Free next day<br>uk delivery</div>
<div class="feature" style="left:300px"><div class="icon"><svg width="40" height="52" viewBox="0 0 40 52"><circle cx="20" cy="18" r="16" fill="var(--green)"/><path d="M10 30l-6 20 16-8 16 8-6-20z" fill="var(--green)"/><path d="M13 18l5 5 9-10" stroke="#fff" stroke-width="3" fill="none"/></svg></div>Regulated and<br>certified</div>
<div class="feature" style="left:520px"><div class="icon"><svg width="50" height="50" viewBox="0 0 50 50"><circle cx="25" cy="25" r="20" fill="none" stroke="var(--green)" stroke-width="5"/><text x="25" y="32" font-size="18" font-weight="800" fill="var(--green)" text-anchor="middle" font-family="Poppins,sans-serif">24</text></svg></div>24/7 customer<br>support</div>
<div class="feature" style="left:740px"><div class="icon"><svg width="54" height="40" viewBox="0 0 54 40"><rect x="2" y="4" width="44" height="30" rx="4" fill="var(--green)"/><rect x="2" y="11" width="44" height="6" fill="#fff"/><rect x="36" y="22" width="16" height="14" rx="2" fill="var(--green-dark)"/></svg></div>Safe &amp; secure<br>payments</div>
<div class="feature" style="left:960px"><div class="icon"><svg width="54" height="46" viewBox="0 0 54 46"><path d="M27 26c-14-9-18-16-12-22 5-4 10-1 12 3 2-4 7-7 12-3 6 6 2 13-12 22z" fill="var(--green)"/><path d="M3 34c8 0 12 6 24 6s16-4 24-10" stroke="var(--green)" stroke-width="5" fill="none" stroke-linecap="round"/></svg></div>10% charity<br>donation</div>

<div class="figure" role="img" aria-label="Husky mascot flying with red cape, with soft shadow" style="left:120px;top:4712px;width:200px;height:230px;background:linear-gradient(180deg,#ececf0 0%,#f1f1f4 100%);box-shadow:0 16px 24px rgba(0,0,0,.12)"></div>
<div class="abs h-big" style="left:250px;top:4722px;width:700px;text-align:center;font-size:54px;line-height:1.08">SO HOW ABOUT YOU<br>GIVE IT A TRY?</div>
<div class="btn" style="left:510px;top:4864px;width:180px;height:46px"><svg class="paw" viewBox="0 0 16 16"><ellipse cx="8" cy="11" rx="4" ry="3.4" fill="#fff"/><circle cx="3" cy="6.5" r="1.7" fill="#fff"/><circle cx="6" cy="3.5" r="1.7" fill="#fff"/><circle cx="10" cy="3.5" r="1.7" fill="#fff"/><circle cx="13" cy="6.5" r="1.7" fill="#fff"/></svg>Join forces!</div>

<footer>
  <div class="abs flabel" style="left:166px;top:4986px">Country/region</div>
  <div class="abs select">United Kingdom (GBP £)<svg width="10" height="6" viewBox="0 0 10 6"><path d="M1 1l4 4 4-4" stroke="#141414" stroke-width="1.6" fill="none"/></svg></div>
  <div class="abs flabel" style="left:616px;top:4986px">Payment method</div>
  <div class="abs pay"><i></i><i></i><i></i><i></i><i></i><i></i><i></i><i style="background:#b39ae8;border-color:#a489de"></i><i></i></div>
  <div class="abs" style="left:70px;top:5098px;width:1060px;height:1px;background:#e3e3e3"></div>
  <div class="abs" style="left:0;width:1200px;top:5110px;text-align:center;font-size:10px;font-weight:600">© 2022, ZEPHYR QUILL UK</div>
  <div class="abs" style="left:1132px;top:5066px;width:54px;height:54px;border-radius:50%;background:#141414;display:flex;align-items:center;justify-content:center"><svg width="26" height="22" viewBox="0 0 26 22"><path d="M13 2c6 0 11 3.6 11 8.3S19 18.6 13 18.6c-1.4 0-2.7-.2-3.9-.5L4 20.5l1.4-4C3.3 15 2 12.8 2 10.3 2 5.6 7 2 13 2z" fill="#fff"/><circle cx="8.5" cy="10.3" r="1.5" fill="#141414"/><circle cx="13" cy="10.3" r="1.5" fill="#141414"/><circle cx="17.5" cy="10.3" r="1.5" fill="#141414"/></svg></div>
</footer>

</body>
</html>
```